Design uplift of Quillamber.com site

The site needs to be fast and responsive down to mobile.
Needs to use the supplied Video as the homepage background.
Needs to use Generate Press as the theme - Site theme to be a child theme of Generate Press.
Needs to have a button above the fold for an offer of a free email course on how to set up a medical software project.
Needs to use the Quillamber logo. This logo has been trademarked.

The existing site is at: www.quillamber.com

```html
<!DOCTYPE html>
<html lang="en">
<head>
<meta charset="utf-8">
<title>Quillamber — Innovative solutions for health software businesses</title>
<link href="https://fonts.googleapis.com/css2?family=Lato:wght@400;700;900&display=swap" rel="stylesheet">
<style>
:root{
  --blue:#039be5;
  --blue-light:#7cc4ee;
  --ink:#1c1c1c;
  --text:#333;
  --grey-bg:#f3f3f3;
  --white:#fff;
  --hero-a:#1d4f78;
  --hero-b:#5f93b8;
}
*{margin:0;padding:0;box-sizing:border-box}
html,body{width:1200px;height:3202px;overflow:hidden}
body{position:relative;font-family:'Lato',sans-serif;color:var(--text);background:var(--white)}
.abs{position:absolute}
.shapes{position:absolute;left:0;top:0;width:1200px;height:3202px}

/* header */
.brand{display:flex;align-items:center;gap:12px;font-weight:700;font-size:32px;color:var(--ink)}
.brand-dot{width:54px;height:54px;border-radius:50%;background:var(--blue)}
.site-brand{left:77px;top:23px}
.nav{left:443px;top:44px;display:flex;font-size:14px;font-weight:700;color:var(--ink);letter-spacing:.3px}
.nav a{position:absolute;white-space:nowrap;color:inherit;text-decoration:none}
.btn-small{top:32px;height:40px;width:92px;background:var(--blue);color:var(--white);font-size:14px;font-weight:700;display:flex;align-items:center;justify-content:center}

/* hero */
.hero-media{left:0;top:100px;width:1200px;height:746px;background:linear-gradient(120deg,var(--hero-a),var(--hero-b) 55%,#2d6a95)}
.hero-text{left:0;width:1200px;text-align:center;color:var(--white);text-shadow:0 2px 6px rgba(0,0,0,.35)}
.hero-kicker{top:268px;font-size:70px;font-weight:900;line-height:1}
.hero-title{top:330px;font-size:100px;font-weight:900;line-height:1;letter-spacing:1px}
.hero-tagline{top:430px;font-size:40px;font-weight:700}
.btn{background:var(--blue);color:var(--white);font-weight:700;display:flex;align-items:center;justify-content:center}
.hero-offer{left:428px;top:504px;width:344px;height:61px;font-size:20px}
.hero-play{left:0;width:1200px;top:596px;display:flex;justify-content:center;align-items:center;gap:8px;color:var(--white);font-size:19px;font-weight:700}
.hero-play span{text-decoration:underline;text-underline-offset:4px}
.dots{display:flex;gap:10px}
.dots i{width:15px;height:15px;border-radius:50%;background:var(--white);display:block}
.dots i.on{background:var(--blue)}
.hero-dots{left:554px;top:764px}

/* welcome */
.photo{background:linear-gradient(135deg,#c9ccd0,#8c9096 55%,#5b6168)}
.welcome-photo{left:81px;top:943px;width:500px;height:379px}
.welcome-title{left:614px;top:958px;font-size:35px;font-weight:900;color:var(--ink)}
.welcome-lead{left:614px;top:1012px;width:500px;font-size:19px;font-weight:700;color:var(--blue);line-height:29px}
.body-copy{font-size:16.5px;line-height:29.5px;color:var(--text)}
.welcome-body{left:614px;top:1084px;width:520px}
.btn-read{width:197px;height:62px;font-size:19px}

/* services */
.section-title{left:0;width:1200px;text-align:center;font-size:35px;font-weight:900;color:var(--ink)}
.service-title{left:75px;top:1638px;font-size:27.5px;font-weight:900;color:var(--blue)}
.service-body{left:75px;top:1683px;width:490px}
.service-body p+p{margin-top:10px}
.service-photo{left:624px;top:1593px;width:501px;height:379px;background:linear-gradient(135deg,#3a4048,#6f7b88 50%,#2f5f93)}

/* blog */
.blog-media{left:75px;top:2210px;width:1050px;height:436px;background:linear-gradient(120deg,#1f252d,#3a4552 55%,#1c2128)}
.blog-card{left:75px;top:2282px;width:512px;height:295px;background:rgba(236,236,236,.93);clip-path:polygon(0 0,100% 0,92% 100%,0 100%)}
.blog-title{left:96px;top:2308px;width:440px;font-size:29px;font-weight:900;color:var(--blue);line-height:31px}
.blog-body{left:97px;top:2416px;width:420px;font-size:16.5px;line-height:28px;color:#444}
.blog-more{left:97px;top:2484px;font-size:15px;font-weight:700;color:var(--blue)}
.blog-dots{left:97px;top:2530px}
.blog-dots i{width:11px;height:11px;background:#555;margin-right:12px}
.blog-dots i.on{background:var(--blue)}
.blog-dots{gap:0}

/* footer */
.footer-bg{left:0;top:2733px;width:1200px;height:411px;background:var(--grey-bg)}
.footer-brand{left:0;width:1200px;top:2801px;justify-content:center;font-size:30px}
.footer-brand .brand-dot{width:50px;height:50px}
.footer-col h4{font-size:16.5px;font-weight:900;color:var(--ink);margin-bottom:12px;white-space:nowrap}
.footer-col li{list-style:none;font-size:12.5px;font-weight:700;color:var(--ink);line-height:30px;white-space:nowrap}
.footer-col{top:2915px}
.contact-col h4{font-weight:700}
.contact-row{display:flex;gap:16px;font-size:12.5px;font-weight:700;color:var(--ink);line-height:21px;margin-bottom:9px}
.contact-row svg{flex:none;margin-top:5px}
.newsletter{left:823px;top:2957px;width:302px;height:41px;border:1px solid var(--blue);background:var(--white);display:flex}
.newsletter span{flex:1;padding-left:10px;font-size:15px;color:#555;line-height:39px}
.newsletter b{width:53px;background:var(--blue);color:var(--white);font-size:17px;display:flex;align-items:center;justify-content:center}
.social{left:825px;top:3036px;display:flex;gap:22px}
.social i{display:block;width:22px;height:22px;border-radius:50%;background:var(--ink)}
.copyright{left:0;top:3144px;width:1200px;height:58px;background:var(--blue);color:var(--white);font-size:13px;text-align:center;line-height:58px}
</style>
</head>
<body>

<!-- header -->
<div class="abs brand site-brand"><span class="brand-dot"></span>Quillamber</div>
<nav class="abs nav">
  <a style="left:0">HOME</a>
  <a style="left:92px">SERVICES</a>
  <a style="left:205px">ABOUT</a>
  <a style="left:303px">BLOG</a>
  <a style="left:390px">CONTACT</a>
</nav>
<div class="abs btn-small" style="left:929px">LOG IN</div>
<div class="abs btn-small" style="left:1033px;width:92px">REGISTER</div>

<!-- hero -->
<div class="abs hero-media" role="img" aria-label="Background video of a surgical team with digital medical data overlays"></div>

<svg class="shapes" viewBox="0 0 1200 3202" aria-hidden="true">
  <!-- hero bottom wedge -->
  <polygon points="0,752 600,826 1200,752 1200,846 0,846" fill="var(--blue-light)"/>
  <polygon points="0,802 600,846 1200,802 1200,846 0,846" fill="#fff"/>
  <!-- welcome frame -->
  <polyline points="70,1132 70,929 293,929" fill="none" stroke="var(--blue)" stroke-width="7"/>
  <!-- services band -->
  <polygon points="0,1470 600,1418 1200,1470 1200,2030 600,2083 0,2030" fill="var(--grey-bg)"/>
  <polygon points="0,1465 600,1418 1200,1465 1200,1483 600,1426 0,1483" fill="var(--blue)"/>
  <polygon points="0,2017 600,2075 1200,2017 1200,2034 600,2083 0,2034" fill="var(--blue)"/>
  <!-- footer top edge -->
  <polygon points="0,2765 600,2733 1200,2765 1200,2800 0,2800" fill="var(--grey-bg)"/>
  <polygon points="0,2765 600,2733 1200,2765 1200,2798 600,2742 0,2798" fill="var(--blue)"/>
</svg>

<div class="abs hero-text hero-kicker">WELCOME TO</div>
<div class="abs hero-text hero-title">QUILLAMBER</div>
<div class="abs hero-text hero-tagline">Innovative solutions for health software businesses</div>
<div class="abs btn hero-offer">OFFER OF A FREE EMAIL COURSE</div>
<div class="abs hero-play">
  <svg width="18" height="18" viewBox="0 0 18 18"><circle cx="9" cy="9" r="9" fill="#fff"/><polygon points="7,5 13,9 7,13" fill="#2d6a95"/></svg>
  <span>PLAY VIDEO</span>
</div>
<div class="abs dots hero-dots"><i class="on"></i><i></i><i></i><i></i></div>

<!-- welcome -->
<div class="abs photo welcome-photo" role="img" aria-label="Developers working together at computers in a bright office"></div>
<svg class="abs" style="left:500px;top:1249px" width="88" height="80" viewBox="0 0 88 80" aria-hidden="true"><polygon points="88,0 88,80 0,80" fill="var(--blue)"/></svg>
<h1 class="abs welcome-title">WELCOME TO OUR WEBSITE</h1>
<p class="abs welcome-lead">Quillamber was founded in 1998. We have helped many customers achieve their dreams.</p>
<p class="abs body-copy welcome-body">Quillamber’ mission is to provide a custom software development service across a range of technologies by using best practice agile methodologies and tools to deliver customer value on time<br>and within budget.</p>
<div class="abs btn btn-read" style="left:614px;top:1236px">READ MORE</div>

<!-- services -->
<h2 class="abs section-title" style="top:1506px;left:14px">OUR SERVICES</h2>
<h3 class="abs service-title">CUSTOM SOFTWARE DEVELOPMENT</h3>
<div class="abs body-copy service-body">
  <p>Using carefully selected software tools and carefully designed custom applications can make running your business so much more enjoyable.</p>
  <p>Quillamber can provide an upfront quote and regular progress updates on your project to give you piece of mind.</p>
</div>
<div class="abs btn btn-read" style="left:75px;top:1869px">READ MORE</div>
<svg class="abs" style="left:910px;top:1575px" width="235" height="350" viewBox="0 0 235 350" aria-hidden="true"><polyline points="2,3.5 227,3.5 227,350" fill="none" stroke="var(--blue)" stroke-width="7"/></svg>
<div class="abs service-photo" role="img" aria-label="Two colleagues reviewing code on a desktop monitor while taking notes"></div>
<svg class="abs" style="left:617px;top:1900px" width="88" height="78" viewBox="0 0 88 78" aria-hidden="true"><polygon points="0,0 88,78 0,78" fill="var(--blue)"/></svg>

<!-- blog -->
<h2 class="abs section-title" style="top:2139px">BLOG POST</h2>
<div class="abs blog-media" role="img" aria-label="Hand pointing at a rising golden line graph over a dark grid with finance icons"></div>
<div class="abs blog-card"></div>
<h3 class="abs blog-title">The Absolutely Unbeatable Way Of Estimating Custom Software Projects</h3>
<p class="abs blog-body">Successful projects require accurate estimates of the effort required to deliver on the project requirements.</p>
<div class="abs blog-more">READ MORE</div>
<div class="abs dots blog-dots"><i class="on"></i><i></i><i></i><i></i></div>

<!-- footer -->
<div class="abs footer-bg"></div>
<svg class="shapes" viewBox="0 0 1200 3202" aria-hidden="true" style="pointer-events:none">
  <polygon points="0,2765 600,2733 1200,2765 1200,2798 600,2742 0,2798" fill="var(--blue)"/>
  <polygon points="0,2798 600,2742 1200,2798 1200,2810 0,2810" fill="var(--grey-bg)"/>
</svg>
<div class="abs brand footer-brand"><span class="brand-dot"></span>Quillamber</div>

<div class="abs footer-col" style="left:75px">
  <h4>SITE MAP</h4>
  <ul><li>HOME</li><li>SERVICES</li><li>ABOUT</li><li>CONTACT</li><li>BLOG</li></ul>
</div>
<div class="abs footer-col" style="left:255px">
  <h4>KEY FEATURES</h4>
  <ul><li>COLLABORATIVE DESIGN PROCESS</li><li>UPFRONT QUOTE</li><li>PROGRESS UPDATES</li></ul>
</div>
<div class="abs footer-col contact-col" style="left:540px">
  <h4>CONTACT INFO</h4>
  <div class="contact-row" style="margin-top:18px">
    <svg width="10" height="12" viewBox="0 0 10 12"><path d="M5 0a4 4 0 0 1 4 4c0 3-4 8-4 8S1 7 1 4a4 4 0 0 1 4-4z" fill="#1c1c1c"/><circle cx="5" cy="4" r="1.5" fill="#f3f3f3"/></svg>
    <span>17 WATTLE CREST ROAD<br>BROOKHAVEN QUEENSLAND 4209<br>AUSTRALIA</span>
  </div>
  <div class="contact-row">
    <svg width="10" height="11" viewBox="0 0 10 11"><path d="M1 1l3 0 1 3-2 1c1 2 2 3 4 4l1-2 3 1v3C5 11 0 6 1 1z" fill="#1c1c1c"/></svg>
    <span>+61 400 555 018</span>
  </div>
  <div class="contact-row">
    <svg width="11" height="9" viewBox="0 0 11 9"><rect width="11" height="9" fill="#1c1c1c"/><polyline points="0,0 5.5,5 11,0" fill="none" stroke="#f3f3f3" stroke-width="1.2"/></svg>
    <span>HELLO@QUILLAMBER.COM</span>
  </div>
</div>
<div class="abs footer-col" style="left:823px">
  <h4 style="font-weight:700">SUBSCRIBE NEWSLETTER</h4>
</div>
<div class="abs newsletter"><span>Enter Email Address</span><b>GO</b></div>
<div class="abs social" aria-label="Social media links"><i></i><i></i><i></i><i></i><i></i></div>

<div class="abs copyright">Copyright © 2022. Company Name All Right Reserved</div>

</body>
</html>
```